The billboard should communicate confidence, energy and approachability while maintaining a professional, premium feel. Rather than relying on a standard agent photograph, property collage or crowded list of services, we would like an original creative idea that makes people look twice. This could involve a fun visual, clever headline, striking colour contrast or an unexpected real estate theme. The concept should feel positive and contemporary, with enough personality to become recognisable throughout the local community.

The key message should appeal to homeowners who are thinking about selling, preparing to sell or simply curious about the value of their property. Copy must be short, clear and conversational, supported by a direct call to action. The agent’s name, phone number and company branding should remain highly visible without competing with the main idea.

The finished billboard will measure 8.0 metres wide by 2.08 metres high (1224px x 324px), so the composition must suit a long landscape format. All important text and imagery should remain comfortably within safe margins and be legible from a distance. The design should avoid small writing, unnecessary detail and visual clutter.

The goal is to create a billboard that feels different from every other real estate sign in the area—something engaging, confident and easy to remember. It should build strong brand awareness, generate conversations and encourage local property owners to contact the agent when they are ready to make their next move. The concept should be adaptable for future campaigns, helping establish a consistent, distinctive and trusted local brand presence.

Target Market(s)

ages 30+

Industry/Entity Type

Real Estate

Requirements
Must have
• call Wade and phone number 0417 63 28 05
Nice to have
• Nice bright and yellow.. Exciting and grabbing

```html
<!DOCTYPE html>
<html lang="en">
<head>
<meta charset="utf-8">
<title>Call Wade – Billboard</title>
<link href="https://fonts.googleapis.com/css2?family=Bebas+Neue&family=Kaushan+Script&family=Montserrat:wght@800&family=Satisfy&display=swap" rel="stylesheet">
<style>
  :root {
    --stage: #333333;
    --brand-yellow: #ffe815;
    --ink: #111111;
    --card: #ffffff;
    --card-edge: #e6e6e6;
    --photo-dark: #5a5514;
    --photo-light: #b8ad2a;
    --rule: #6b6412;
  }
  * { margin: 0; padding: 0; box-sizing: border-box; }
  html, body {
    width: 1200px; height: 1001px; overflow: hidden;
    background: var(--stage);
  }
  .billboard {
    position: absolute; left: 126px; top: 376px;
    width: 948px; height: 246px;
    background: var(--brand-yellow);
    overflow: hidden;
  }
  .property-photo {
    position: absolute; left: 0; top: 100px;
    width: 230px; height: 146px;
    background: linear-gradient(160deg, var(--photo-light), var(--photo-dark));
  }
  .cta-tab {
    position: absolute; left: 238px; top: 198px;
    width: 190px; height: 34px;
    background: var(--ink);
  }
  .price-tag {
    position: absolute; left: 104px; top: 40px;
    width: 320px; height: 166px;
    border-radius: 12px;
    transform: rotate(12deg);
  }
  .price-tag--back {
    background: var(--card-edge);
    left: 112px; top: 50px;
  }
  .price-tag--front {
    background: var(--card);
    box-shadow: 0 2px 6px rgba(0,0,0,.25);
  }
  .headline {
    position: absolute; left: 40px; top: 8px;
    font-family: "Bebas Neue", sans-serif;
    font-size: 62px; line-height: 48px;
    color: #1b1b1b;
    letter-spacing: 1px;
    white-space: nowrap;
  }
  .contact {
    position: absolute; left: 488px; top: 0; width: 370px; height: 246px;
  }
  .call-line {
    position: absolute; left: 0; right: 0; top: 18px;
    text-align: center;
    font-family: "Kaushan Script", cursive;
    font-size: 62px; line-height: 1;
    color: var(--ink);
    white-space: nowrap;
  }
  .call-swoosh { position: absolute; left: 50px; top: 80px; }
  .phone {
    position: absolute; left: -20px; right: -20px; top: 110px;
    text-align: center;
    font-family: "Bebas Neue", sans-serif;
    font-size: 74px; line-height: 1;
    color: var(--ink);
    white-space: nowrap;
  }
  .rule {
    position: absolute; left: 0; right: 0; top: 186px;
    height: 1px; background: var(--rule);
  }
  .brand-row {
    position: absolute; left: 0; right: 0; top: 202px; height: 34px;
    display: flex; align-items: center;
    white-space: nowrap;
  }
  .brand-name {
    font-family: "Montserrat", sans-serif; font-weight: 800;
    font-size: 19px; color: var(--ink);
    width: 160px;
  }
  .brand-divider {
    width: 1.5px; height: 32px; background: var(--ink); margin: 0 12px 0 4px;
  }
  .tagline {
    font-family: "Satisfy", cursive;
    font-size: 18px; color: var(--ink);
  }
</style>
</head>
<body>
  <div class="billboard">
    <div class="property-photo" role="img" aria-label="Yellow-tinted photo of a modern two-storey home at dusk"></div>
    <div class="cta-tab"></div>
    <div class="price-tag price-tag--back"></div>
    <div class="price-tag price-tag--front">
      <div class="headline">What's<br>your home<br>worth?</div>
    </div>

    <div class="contact">
      <div class="call-line">Call Wade</div>
      <svg class="call-swoosh" width="270" height="14" viewBox="0 0 270 14">
        <path d="M2 11 C 90 2, 190 0, 268 6 C 190 4, 100 6, 2 11 Z" fill="#111"/>
      </svg>
      <div class="phone">0417 63 28 05</div>
      <div class="rule"></div>
      <div class="brand-row">
        <span class="brand-name">Lorne Bexley</span>
        <span class="brand-divider"></span>
        <span class="tagline">You property. Our priority</span>
      </div>
    </div>
  </div>
</body>
</html>
```